TORM PTY LTD - Business Cards

Design a modern business card - using the attached Designs.
Same design as on the front, apart from the names/numbers/emails to be different.
We want the cards to be very glossy to stand out, do I think the simple black/white/metallic will be effective.
Both lots of details below:

Kyle Fornaby
Director
kyle_torm@quillnet.example
0491 382 604

Martin Slade
Director
marty_torm@quillnet.example
0418 305 249

```html
<!DOCTYPE html>
<html lang="en">
<head>
<meta charset="utf-8">
<title>Fornaby Slade – Business Cards</title>
<link rel="stylesheet" href="https://fonts.googleapis.com/css2?family=Inter:ital,wght@0,200;0,300;0,800;1,200&display=swap">
<style>
  :root {
    --canvas: #d9d9d9;
    --card: #060606;
    --ink-strong: #f2f2f2;
    --ink-soft: #9a9a9a;
    --ink-muted: #6f6f6f;
    --metal: #bdbdbd;
    --metal-dark: #3a3a3a;
  }
  * { box-sizing: border-box; margin: 0; padding: 0; }
  html, body {
    width: 1200px;
    height: 1200px;
    overflow: hidden;
    background: var(--canvas);
    font-family: "Inter", "Helvetica Neue", Arial, sans-serif;
  }
  .sheet {
    width: 1200px;
    height: 1200px;
    display: flex;
    flex-direction: column;
    align-items: center;
    justify-content: center;
    gap: 56px;
  }
  .card {
    position: relative;
    width: 840px;
    height: 513px;
    background: var(--card);
    border-radius: 4px;
    box-shadow: 0 10px 28px rgba(0,0,0,0.25);
    overflow: hidden;
  }

  /* Back: brand name */
  .card--back {
    display: flex;
    align-items: center;
    justify-content: center;
  }
  .brand {
    display: flex;
    align-items: center;
    gap: 24px;
  }
  .brand__dot {
    flex: none;
    width: 72px;
    height: 72px;
    border-radius: 50%;
    background: var(--metal-dark);
  }
  .brand__name {
    font-weight: 800;
    font-size: 62px;
    letter-spacing: 3px;
    color: var(--metal);
    line-height: 1;
    white-space: nowrap;
  }

  /* Front: contact details */
  .contact {
    position: absolute;
    left: 62px;
    top: 56px;
    font-weight: 300;
    font-size: 27px;
    line-height: 1.3;
    color: var(--ink-soft);
  }
  .brand--small {
    position: absolute;
    right: 50px;
    top: 150px;
    gap: 10px;
  }
  .brand--small .brand__dot { width: 26px; height: 26px; }
  .brand--small .brand__name { font-size: 22px; letter-spacing: 1px; }
  .person {
    position: absolute;
    left: 62px;
    top: 232px;
  }
  .person__name {
    font-weight: 800;
    font-size: 64px;
    letter-spacing: 1px;
    color: var(--ink-strong);
    line-height: 1.1;
    text-transform: uppercase;
  }
  .person__role {
    margin-left: 170px;
    font-weight: 200;
    font-style: italic;
    font-size: 46px;
    color: var(--ink-muted);
    line-height: 1.2;
  }
</style>
</head>
<body>
  <main class="sheet">
    <section class="card card--back" aria-label="Card back">
      <div class="brand">
        <span class="brand__dot"></span>
        <span class="brand__name">FORNABY SLADE</span>
      </div>
    </section>

    <section class="card card--front" aria-label="Card front">
      <div class="contact">
        <p class="contact__email">kyle_torm@quillnet.example</p>
        <p class="contact__phone">0491 382 604</p>
      </div>
      <div class="brand brand--small">
        <span class="brand__dot"></span>
        <span class="brand__name">FORNABY SLADE</span>
      </div>
      <div class="person">
        <h1 class="person__name">Kyle Fornaby</h1>
        <p class="person__role">Director</p>
      </div>
    </section>
  </main>
</body>
</html>
```